Successfully Managing through a Hurricane Training Event

This learning event is specifically for Birch Supply retailers/stores located outside of the US who are seeking guidance and help with how to plan, prepare, manage there business during Hurricane/Tropical Storm season.

----------------------------------------------
Event Title: Successfully Managing Through Hurricane Season

Event Description: Hurricanes and severe tropical storms are some of the most devastating, and costly, natural disasters known to humans. In fact, historically, 40% of small businesses impacted by a natural disaster do not reopen. If your business is vulnerable to these potential catastrophic events, it is important to develop an effective preparedness and mitigation plan, and take prompt action. Doing so will not only increase the safety of your store associates and customers, but it will help you remain in business after a hurricane strikes, improving your community’s ability to recover. This session focuses on:

o In-store preparation functions
o Implementing business continuity operating procedures for protecting and maintaining your business
o Sustaining the capability to provide products to customers
o Building a hurricane-ready optimized assortment of in-demand products, including special merchandising opportunities
o Deploying effective inventory management and system strategies for staying in stock
o Knowing your available contacts and rules of engagement
o Preserving a competitive advantage and reputation
o Optimizing the means by which you leverage your freight forwarding facility

Event is hosted by: Birch Worldwide Solutions www.birchworldservicesgroup.example

Logistical Details:
• Length: 1 hour
• Date: Friday, August 17, 2018
• Time: 1:00 – 2:00 p.m.

To Register for this Event, Go To: https://www.tovrelin.example/bir18/fall/

Pricing: $ 25 per participant
*Charged to Invoice post-show

Questions? For more information, contact Martin Olsby
+1 555-014-2836
molsby@birchsupply.example

Target Market(s)

Birch Supply International Stores

Industry/Entity Type

Retail

Font styles to use
Serif

Requirements
Must have
• See Word File Attachment
• Use Birch Supply red and black logo colors.
• 1 -Sided brochure
Nice to have
Should not have
• N/A

```html
<!DOCTYPE html>
<html lang="en">
<head>
<meta charset="utf-8">
<title>Successfully Managing Through Hurricane Season</title>
<link rel="stylesheet" href="https://fonts.googleapis.com/css2?family=Teko:wght@400;500&family=Roboto:wght@400;500;700&display=swap">
<style>
  :root {
    --red: #d0202e;
    --red-deep: #a3101c;
    --red-dark: #7a0b14;
    --black: #1c1c1e;
    --ink: #2a2a2a;
    --white: #ffffff;
    --backdrop: #d6d6d6;
  }
  * { box-sizing: border-box; margin: 0; padding: 0; }
  html, body { width: 1200px; height: 687px; overflow: hidden; background: var(--backdrop); }
  body { position: relative; font-family: "Roboto", Arial, sans-serif; color: var(--ink); }

  .flyer {
    position: absolute; left: 367px; top: 14px;
    width: 446px; height: 630px;
    background: var(--white);
    transform: scale(1.045); transform-origin: top left;
    overflow: hidden;
    box-shadow: 0 6px 18px rgba(0,0,0,.18);
  }
  .flyer-shapes { position: absolute; inset: 0; }
  .storm-photo { position: absolute; inset: 0; }

  .brand { position: absolute; left: 20px; top: 30px; display: flex; align-items: center; gap: 8px; }
  .brand-dot { width: 28px; height: 28px; border-radius: 50%; background: var(--red); }
  .brand-name { font-family: "Roboto", sans-serif; font-weight: 500; font-size: 15px; color: var(--black); line-height: 1; }

  .headline {
    position: absolute; left: 13px; top: 124px;
    font-family: "Teko", "Arial Narrow", sans-serif; font-weight: 500;
    font-size: 36px; line-height: 31px; color: var(--white); letter-spacing: .3px;
  }
  .headline .accent { color: var(--red); }

  .event-when { position: absolute; left: 14px; top: 247px; color: var(--white); font-size: 13.5px; line-height: 19px; }
  .event-when div { display: flex; align-items: center; gap: 6px; }
  .event-when svg { width: 11px; height: 11px; }

  .intro { position: absolute; left: 11px; top: 318px; width: 424px; font-size: 6.3px; line-height: 8.3px; color: var(--ink); }

  .focus-tag {
    position: absolute; left: 128px; top: 370px; width: 188px; height: 16px;
    border-radius: 8px; background: var(--red-deep); border: 1px solid var(--white);
    color: var(--white); font-size: 10px; font-weight: 500; text-align: center; line-height: 14px;
  }
  .focus-list { position: absolute; top: 394px; list-style: none; color: var(--white); font-size: 6.2px; line-height: 8.5px; }
  .focus-list li { position: relative; padding-left: 12px; margin-bottom: 2px; }
  .focus-list li::before { content: ""; position: absolute; left: 2px; top: 2.5px; width: 3.5px; height: 3.5px; border-radius: 50%; background: var(--white); }
  .focus-left { left: 12px; width: 210px; }
  .focus-right { left: 236px; width: 200px; }

  .pricing { position: absolute; left: 0; width: 100%; top: 478px; text-align: center; font-size: 19px; color: var(--black); letter-spacing: .2px; }
  .pricing strong { color: var(--red); font-weight: 700; }
  .pricing-note { position: absolute; left: 0; width: 100%; top: 502px; text-align: center; font-size: 8.5px; }
  .register-note { position: absolute; left: 0; width: 100%; top: 526px; text-align: center; font-size: 7.5px; }
  .register-url {
    position: absolute; left: 78px; top: 538px; width: 288px; height: 19px; border-radius: 10px;
    background: var(--red-dark); color: var(--white); text-align: center; font-size: 12px; font-weight: 500; line-height: 19px;
  }
  .host { position: absolute; left: 0; width: 100%; top: 566px; text-align: center; font-size: 8.5px; color: var(--black); }
  .host strong { color: var(--red); font-weight: 700; }

  .questions { position: absolute; left: 62px; top: 583px; color: var(--white); }
  .questions .q-title { color: var(--red); font-size: 12px; font-weight: 500; line-height: 13px; }
  .questions .q-sub { font-size: 7.5px; line-height: 10px; }
  .questions .q-name { color: var(--red); font-size: 13.5px; font-weight: 700; line-height: 17px; }
  .footer-divider { position: absolute; left: 215px; top: 590px; width: 1px; height: 32px; background: #555; }
  .contact { position: absolute; left: 245px; top: 586px; list-style: none; color: var(--white); font-size: 7.5px; line-height: 11.5px; }
  .contact li { display: flex; align-items: center; gap: 6px; }
  .contact svg { width: 6px; height: 6px; fill: var(--red); }
</style>
</head>
<body>
<main class="flyer">
  <svg class="flyer-shapes" viewBox="0 0 446 630" aria-hidden="true">
    <rect x="0" y="90" width="446" height="212" fill="var(--black)"/>
    <polygon points="290,0 320,0 232,90 200,90" fill="var(--red)"/>
    <polygon points="256,0 270,0 182,90 168,90" fill="var(--red-deep)"/>
    <polygon points="0,245 228,245 240,290 0,290" fill="var(--red)"/>
    <rect x="0" y="374" width="446" height="96" fill="var(--red-deep)"/>
    <path d="M0,584 Q120,570 446,578 L446,630 L0,630 Z" fill="var(--black)"/>
    <path d="M0,588 Q20,575 60,578 L30,630 L0,630 Z" fill="var(--red)"/>
    <path d="M446,570 Q430,572 420,584 L446,588 Z" fill="var(--red)"/>
  </svg>
  <svg class="storm-photo" viewBox="0 0 446 630" role="img" aria-label="Photo of a pickup truck driving through flooded road in a hurricane with bent palm trees">
    <defs>
      <linearGradient id="stormTone" x1="0" y1="0" x2="0" y2="1">
        <stop offset="0" stop-color="#c9cfcf"/>
        <stop offset=".6" stop-color="#9aa3a3"/>
        <stop offset="1" stop-color="#d7dbda"/>
      </linearGradient>
    </defs>
    <polygon points="322,0 446,0 446,302 332,302 218,192 218,100" fill="url(#stormTone)"/>
  </svg>

  <div class="brand"><span class="brand-dot"></span><span class="brand-name">Birch Worldwide Solutions</span></div>

  <h1 class="headline">Successfully<br>Managing Through<br><span class="accent">Hurricane Season</span></h1>

  <div class="event-when">
    <div><svg viewBox="0 0 10 10"><rect x="1" y="1.5" width="8" height="7.5" fill="none" stroke="#fff"/><line x1="1" y1="4" x2="9" y2="4" stroke="#fff"/></svg>Friday, August 17, 2018</div>
    <div><svg viewBox="0 0 10 10"><circle cx="5" cy="5" r="4" fill="none" stroke="#fff"/><path d="M5 2.5V5l2 1" fill="none" stroke="#fff"/></svg>1:00 – 2:00 p.m.</div>
  </div>

  <p class="intro">Hurricanes and severe tropical storms are some of the most devastating, and costly, natural disasters known to humans. In fact, historically, 40% of small businesses impacted by a natural disaster do not reopen. If your business is vulnerable to these potential catastrophic events, it is important to develop an effective preparedness and mitigation plan, and take prompt action. Doing so will not only increase the safety of your store associates and customers, but it will help you remain in business after a hurricane strikes, improving your community’s ability to recover.</p>

  <div class="focus-tag">THIS SESSION FOCUSES ON</div>
  <ul class="focus-list focus-left">
    <li>In-store preparation functions</li>
    <li>Implementing business continuity operating procedures for protecting and maintaining your business</li>
    <li>Sustaining the capability to provide products to customers</li>
    <li>Building a hurricane-ready optimized assortment of in-demand products, including special merchandising opportunities</li>
  </ul>
  <ul class="focus-list focus-right">
    <li>Deploying effective inventory management and system strategies for staying in stock</li>
    <li>Knowing your available contacts and rules of engagement</li>
    <li>Preserving a competitive advantage and reputation</li>
    <li>Optimizing the means by which you leverage your freight forwarding facility</li>
  </ul>

  <p class="pricing">PRICING: <strong>$25 PER</strong> PARTICIPANT</p>
  <p class="pricing-note">*CHARGED TO INVOICE POST-SHOW</p>
  <p class="register-note">To Register for this Event, Go To</p>
  <p class="register-url">https://www.tovrelin.example/bir18/fall/</p>
  <p class="host">Event is hosted by: <strong>BIRCH WORLDWIDE SOLUTIONS</strong></p>

  <div class="questions">
    <p class="q-title">QUESTIONS?</p>
    <p class="q-sub">For more information contact</p>
    <p class="q-name">MARTIN OLSBY</p>
  </div>
  <div class="footer-divider"></div>
  <ul class="contact">
    <li><svg viewBox="0 0 10 10"><path d="M2 1l2 2-1 1.5a6 6 0 0 0 2.5 2.5L7 6l2 2-1.5 1.5C4 9 1 6 .5 2.5z"/></svg>+1 555-014-2836</li>
    <li><svg viewBox="0 0 10 10"><rect x="0" y="2" width="10" height="6"/></svg>molsby@birchsupply.example</li>
    <li><svg viewBox="0 0 10 10"><circle cx="5" cy="5" r="5"/></svg>www.birchworldservicesgroup.example</li>
  </ul>
</main>
</body>
</html>
```